Baby Boutique Needs a Business Card Design

We need a modern double sided business card design using the attached logo for T' Tot Nook.

T' Tot Nook is a baby boutique which sells only handmade clothing and accessories for both boys and girls. Our store will live exclusively online.

We would like to only use the colors that have been used in the logo.

Target Market(s)

Potential wholesale clients, Small business owners

Industry/Entity Type

Retail

Contact Information for Business Card

Name Benedict R. Halvorsen (Owner)
Email sales@ttotnook.example
Main Phone 555-203-7164
Cell phone 555-203-7590
Website www.TTotNook.example

Font styles to use
Sans Serif

Colors

Designer to choose colors to be used in the design.

Requirements
Must have
• -Would like to have icons that indentify the contact information.
• -Include our website
• -Include our tagline in a small area near the bottom. "Handmade Baby Creations"
• -Would like to include Facebook and Instagram Icons
• -
Nice to have
• Would like to have a simple back side with the logo.
• Something along the lines of the meridale funding card attached.

```html
<!DOCTYPE html>
<html lang="en">
<head>
<meta charset="utf-8">
<title>T' Tot Nook – Business Card</title>
<link rel="stylesheet" href="https://fonts.googleapis.com/css2?family=Lato:wght@400;700;900&display=swap">
<style>
  :root {
    --mint: #7fd3c6;
    --coral: #ea7a76;
    --paper: #f4f4f3;
    --night: #2b2627;
    --ink: #6d6a6b;
    --backdrop: #1b1a1b;
  }
  * { box-sizing: border-box; margin: 0; padding: 0; }
  html, body { width: 1200px; height: 900px; overflow: hidden; }
  body {
    background: var(--backdrop);
    font-family: "Lato", Arial, sans-serif;
    position: relative;
  }
  .card {
    position: absolute;
    left: 250px;
    width: 700px;
    height: 400px;
    border-radius: 24px;
    overflow: hidden;
  }
  .card--front { top: 33px; background: var(--paper); }
  .card--back  { top: 467px; background: var(--night); }
  .card-band { position: absolute; inset: 0; width: 700px; height: 400px; }

  .brand {
    position: absolute;
    display: flex;
    align-items: center;
    gap: 14px;
  }
  .brand-dot { width: 22px; height: 22px; border-radius: 50%; background: var(--coral); }
  .brand-name { font-weight: 900; font-size: 50px; color: var(--mint); line-height: 1; }
  .card--front .brand { left: 44px; top: 120px; }
  .card--back .brand { left: 50%; top: 150px; transform: translateX(-50%); }
  .card--back .brand-name { font-size: 62px; }

  .tagline {
    position: absolute;
    left: 40px; top: 347px;
    color: #fff; font-weight: 700; font-size: 18px;
  }
  .divider { position: absolute; width: 3px; }
  .divider--coral { left: 350px; top: 95px; height: 48px; background: var(--coral); }
  .divider--mint  { left: 350px; top: 175px; height: 110px; width: 2px; background: var(--mint); }

  .person { position: absolute; left: 385px; top: 100px; }
  .person-name { color: var(--coral); font-weight: 900; font-size: 27px; }
  .person-role { color: var(--ink); font-size: 17px; margin-top: 2px; }

  .contact-list { position: absolute; left: 385px; top: 195px; list-style: none; }
  .contact-item {
    display: flex; align-items: center; gap: 12px;
    color: var(--ink); font-size: 18px; height: 27px;
  }
  .contact-icon { width: 16px; height: 16px; flex: none; }

  .follow {
    position: absolute; right: 40px; top: 352px;
    display: flex; align-items: center; gap: 8px;
    color: #fff; font-size: 16px; font-weight: 700;
  }
  .follow-dot { width: 20px; height: 20px; border-radius: 50%; background: #fff; opacity: .85; }
</style>
</head>
<body>

<section class="card card--front" aria-label="Card front">
  <svg class="card-band" viewBox="0 0 700 400" aria-hidden="true">
    <path d="M0 322 H300 C320 322 320 364 345 364 H700 V400 H0 Z" fill="var(--mint)"/>
    <path d="M0 330 H300 C320 330 320 374 345 374 H700 V400 H0 Z" fill="var(--coral)"/>
    <path d="M345 374 H700 V390 H345 C330 390 330 390 345 374 Z" fill="var(--mint)" opacity="0"/>
    <rect x="345" y="376" width="355" height="14" fill="var(--mint)"/>
  </svg>

  <div class="brand">
    <span class="brand-name">T' Tot Nook</span>
  </div>

  <p class="tagline">Handmade Baby Creations</p>

  <span class="divider divider--coral"></span>
  <span class="divider divider--mint"></span>

  <div class="person">
    <p class="person-name">Benedict R. Halvorsen</p>
    <p class="person-role">Owner</p>
  </div>

  <ul class="contact-list">
    <li class="contact-item">
      <svg class="contact-icon" viewBox="0 0 16 16"><path d="M4 1 L6 5 L4.5 6.5 C5.5 8.5 7.5 10.5 9.5 11.5 L11 10 L15 12 L13.5 15 C7 14.5 1.5 9 1 2.5 Z" fill="var(--coral)"/></svg>
      555-203-7164
    </li>
    <li class="contact-item">
      <svg class="contact-icon" viewBox="0 0 16 16"><rect x="4" y="1" width="8" height="14" rx="1.5" fill="none" stroke="var(--coral)" stroke-width="1.6"/><circle cx="8" cy="12.5" r="1" fill="var(--coral)"/></svg>
      555-203-7590
    </li>
    <li class="contact-item">
      <svg class="contact-icon" viewBox="0 0 16 16"><rect x="1" y="3" width="14" height="10" rx="1" fill="none" stroke="var(--coral)" stroke-width="1.6"/><path d="M1.5 3.5 L8 9 L14.5 3.5" fill="none" stroke="var(--coral)" stroke-width="1.6"/></svg>
      sales@ttotnook.example
    </li>
    <li class="contact-item">
      <svg class="contact-icon" viewBox="0 0 16 16"><circle cx="8" cy="8" r="6.5" fill="none" stroke="var(--coral)" stroke-width="1.5"/><ellipse cx="8" cy="8" rx="3" ry="6.5" fill="none" stroke="var(--coral)" stroke-width="1.2"/><path d="M1.5 8 H14.5" stroke="var(--coral)" stroke-width="1.2"/></svg>
      www.TTotNook.example
    </li>
  </ul>
</section>

<section class="card card--back" aria-label="Card back">
  <svg class="card-band" viewBox="0 0 700 400" aria-hidden="true">
    <path d="M700 322 H400 C380 322 380 364 355 364 H0 V400 H700 Z" fill="var(--mint)"/>
    <path d="M700 330 H400 C380 330 380 374 355 374 H0 V400 H700 Z" fill="var(--coral)"/>
    <rect x="0" y="376" width="355" height="14" fill="var(--mint)"/>
  </svg>

  <div class="brand">
    <span class="brand-name">T' Tot Nook</span>
  </div>

  <p class="follow">Follow us on <span class="follow-dot"></span><span class="follow-dot"></span></p>
</section>

</body>
</html>
```